Tarnwick Youth Harbor Centers
Gala Invitation
"Opening the Door"
We seek a design for our annual fundraising ball invitation to be held on November 3, 2012. We are a private foundation that operates multiple Youth Harbor Center sites within the city of Chicago.
We would like to see an elegant design, befitting a formal event, but with a modern and sleek tone. We envision black and silver tones, possibly juxtaposed with colorful photos of smiling children. However, we are not married to any one particular design concept or color palette.
While our tagline, "Opening the Door" certainly lends itself to many design posibilities, we would like to see creative and subtle, rather than more obvious interpretations.
For further background on the Youth Harbor Centers Federation, see www.yhcfed-example.org.
This invitation will be sent to our foundation members and prospective guests.
We need an invitation and a matching "save the date card".

```html
<!DOCTYPE html>
<html lang="en">
<head>
<meta charset="utf-8">
<title>Tarnwick Youth Harbor Centers – Gala Invitation</title>
<link rel="stylesheet" href="https://fonts.googleapis.com/css2?family=Merienda:wght@700;900&display=swap">
<style>
  :root {
    --header-bg: #ffffff;
    --header-edge: #b9b9b9;
    --header-ink: #1a1a1a;
    --brand-ink: #2f6fb3;
    --stage-dark: #000000;
    --stage-glow: #3a3a3a;
    --title-ink: #ffffff;
    --photo-warm: #c98a5e;
    --photo-bright: #e9c24a;
    --photo-cool: #4a9ec9;
  }
  * { margin: 0; padding: 0; box-sizing: border-box; }
  html, body {
    width: 1200px;
    height: 811px;
    overflow: hidden;
    background: var(--stage-dark);
  }
  .invitation {
    position: relative;
    width: 1200px;
    height: 811px;
    overflow: hidden;
    font-family: "Merienda", cursive;
    background: radial-gradient(ellipse 50% 55% at 50% 55%, var(--stage-glow) 0%, #1a1a1a 55%, var(--stage-dark) 100%);
  }
  .masthead {
    position: absolute;
    inset: 0 0 auto 0;
    height: 82px;
    background: var(--header-bg);
    border-bottom: 6px solid var(--header-edge);
    display: flex;
    align-items: center;
    justify-content: center;
  }
  .masthead__brand {
    position: absolute;
    left: 18px;
    top: 14px;
    display: flex;
    align-items: center;
    gap: 6px;
    width: 118px;
    font-size: 11px;
    font-weight: 700;
    line-height: 1.2;
    color: var(--brand-ink);
  }
  .masthead__brand-dot {
    flex: none;
    width: 14px;
    height: 14px;
    border-radius: 50%;
    background: var(--brand-ink);
  }
  .masthead__title {
    font-size: 36px;
    font-weight: 700;
    font-style: italic;
    color: var(--header-ink);
  }
  .headline {
    position: absolute;
    top: 168px;
    left: 0;
    width: 100%;
    text-align: center;
    color: var(--title-ink);
  }
  .headline__title {
    font-size: 84px;
    font-weight: 900;
    line-height: 1.05;
    letter-spacing: 1px;
  }
  .headline__tagline {
    font-size: 46px;
    font-weight: 700;
    font-style: italic;
    line-height: 1.2;
  }
  .children-photo {
    position: absolute;
    left: 290px;
    top: 355px;
    width: 610px;
    height: 470px;
    border-radius: 48% 48% 0 0 / 40% 40% 0 0;
    background:
      radial-gradient(circle at 30% 35%, var(--photo-bright) 0%, transparent 35%),
      radial-gradient(circle at 70% 45%, var(--photo-cool) 0%, transparent 35%),
      radial-gradient(circle at 50% 60%, var(--photo-warm) 0%, #6a4a3a 70%, transparent 100%);
    opacity: 0.9;
  }
</style>
</head>
<body>
  <main class="invitation">
    <header class="masthead">
      <div class="masthead__brand">
        <span class="masthead__brand-dot"></span>
        <span>Youth Harbor Centers Federation</span>
      </div>
      <h1 class="masthead__title">Tarnwick Youth Harbor Centers</h1>
    </header>

    <section class="headline">
      <h2 class="headline__title">GALA INVITATION</h2>
      <p class="headline__tagline">"Opening the Door"</p>
    </section>

    <div class="children-photo" role="img" aria-label="Photo of smiling children in colourful shirts standing in a circle, looking up at the camera"></div>
  </main>
</body>
</html>
```